PowerPoint Template Design for business consulting company in Silicon Valley

I need a PowerPoint template to use as the starting point for new presentations. I have a logo but now need design that supports this. I've attached a very descriptive PDF that explains exactly what I need. Here is a list of deliverables: 1. PowerPoint Template that I will use as the starter presentation for all new Lantern Quorix presentationsDesigns for the following slides: See picture below for examples of structure:2. Title slide with subtitle3. Section header4. Title and body5. Title and 2 columns6. Title and 3 columns7. One column text8. Editable timeline to show months, or steps for a process9. Bullet design for unordered list (can be graphic)10. Bullet design for ordered list11. Recommended fonts for each design: Title, subtitle, list, captionOPTIONAL: Possible graphic elements to be used for section title slide backgrounds or graphic elements:--Your team / my team / people on project--Goals for project / presentation--Editable Timeline--Speaking--Writing--Listening--People collaborating / helping each otherI am happy to accept proposals for developing these optional elements in a separate project.

Requirements
Must have
• Must be FLAT design.
• Not flashy or garish. Must be subtle.

```html
<!DOCTYPE html>
<html lang="en">
<head>
<meta charset="utf-8">
<title>Lantern Quorix — Presentation Template</title>
<link rel="stylesheet" href="https://fonts.googleapis.com/css2?family=Lora:wght@400&display=swap">
<style>
  :root {
    --canvas: #f5f6f8;
    --canvas-wave: #fbfbfc;
    --slide: #ffffff;
    --ink: #3a3a3a;
    --ink-soft: #6b6b6b;
    --ink-faint: #d9dbdf;
    --brand-green: #1b7a3e;
    --brand-blue: #1f3f9a;
    --disc: #f6f6f7;
    --leaf: #f3f4f6;
    --shadow: 0 2px 6px rgba(0,0,0,0.12);
  }
  * { box-sizing: border-box; margin: 0; padding: 0; }
  html, body { width: 1200px; height: 1200px; overflow: hidden; }
  body {
    background: var(--canvas);
    font-family: "Lora", serif;
    color: var(--ink);
    position: relative;
  }
  .backdrop { position: absolute; inset: 0; }

  .slide {
    position: absolute;
    background: var(--slide);
    box-shadow: var(--shadow);
    overflow: hidden;
  }
  .slide--title-center { left: 281px; top: 85px; width: 638px; height: 359px; }
  .slide--title-left   { left: 281px; top: 472px; width: 638px; height: 358px; }
  .slide--columns      { left: 39px;  top: 861px; width: 539px; height: 302px; }
  .slide--heavy        { left: 622px; top: 861px; width: 539px; height: 302px; }

  .foliage {
    position: absolute;
    background: radial-gradient(ellipse at 50% 50%, var(--leaf) 0%, rgba(243,244,246,0) 70%);
  }
  .disc { position: absolute; border-radius: 50%; background: var(--disc); }

  .brand {
    position: absolute;
    font-family: "Lora", serif;
    color: var(--brand-green);
    text-align: center;
    line-height: 1.05;
  }
  .brand--large { font-size: 13px; }
  .brand--small { font-size: 7.5px; }

  .headline {
    font-weight: 400;
    letter-spacing: 0.5px;
    white-space: nowrap;
  }
  .headline--gradient {
    background: linear-gradient(90deg, var(--brand-green) 0%, var(--brand-green) 35%, var(--brand-blue) 75%);
    -webkit-background-clip: text;
    background-clip: text;
    color: transparent;
  }
  .rule { height: 1px; background: var(--ink-faint); }
  .detail { font-size: 10.5px; color: var(--ink-soft); letter-spacing: 0.3px; }
  .fineprint {
    position: absolute;
    font-size: 6px;
    letter-spacing: 4px;
    color: var(--ink-faint);
    text-transform: uppercase;
    white-space: nowrap;
  }

  .eyebrow { font-size: 10.5px; color: var(--ink); }
  .slide-title { font-size: 21px; color: var(--ink); font-weight: 400; white-space: nowrap; }

  .step {
    position: absolute;
    top: 100px;
    width: 100px;
    margin-left: -50px;
    text-align: center;
  }
  .step__num {
    width: 26px; height: 26px; margin: 0 auto;
    border-radius: 50%;
    background: var(--disc);
    font-size: 9px; line-height: 26px; color: var(--ink-soft);
  }
  .step__title { margin-top: 8px; font-size: 10px; line-height: 12px; color: var(--ink); }
  .step__rule { width: 28px; height: 1px; background: var(--ink-faint); margin: 4px auto 0; }
  .step__body { margin-top: 10px; font-size: 7.3px; line-height: 11.4px; color: var(--ink-soft); }
  .connector { position: absolute; top: 113px; height: 1px; border-top: 1px dotted var(--ink-faint); }
</style>
</head>
<body>

<svg class="backdrop" width="1200" height="1200" viewBox="0 0 1200 1200" aria-hidden="true">
  <path d="M0 455 L830 370 C1040 345 1130 320 1200 250 L1200 0 L0 0 Z" fill="var(--canvas-wave)"/>
  <path d="M460 1200 C560 1010 800 870 1200 790 L1200 1200 Z" fill="#f2f3f6"/>
</svg>

<!-- Title slide, centered -->
<section class="slide slide--title-center">
  <div class="foliage" role="img" aria-label="Faint bamboo stalks and leaves" style="left:430px;top:0;width:208px;height:359px;"></div>
  <div class="foliage" role="img" aria-label="Faint scattered leaves" style="left:0;top:60px;width:140px;height:280px;"></div>
  <div class="disc" style="left:271px;top:-35px;width:96px;height:96px;"></div>
  <div class="brand brand--large" style="left:269px;top:22px;width:100px;">Lantern<br>Quorix</div>
  <div class="disc" style="left:240px;top:100px;width:160px;height:160px;"></div>
  <div style="position:absolute;left:0;top:132px;width:638px;text-align:center;">
    <h1 class="headline headline--gradient" style="font-size:43px;line-height:50px;">PLACE YOUR</h1>
    <h2 class="headline headline--gradient" style="font-size:26px;line-height:31px;">PRESENTATION TITLE HERE</h2>
    <div class="rule" style="width:50px;margin:5px auto 6px;"></div>
    <p class="detail">MORE DETAIL HERE</p>
  </div>
  <p class="fineprint" style="left:0;width:638px;text-align:center;top:345px;">2018 · Confidential</p>
</section>

<!-- Title slide, left aligned -->
<section class="slide slide--title-left">
  <div class="foliage" role="img" aria-label="Faint bamboo stalks and leaves" style="left:430px;top:0;width:208px;height:358px;"></div>
  <div class="brand brand--large" style="left:22px;top:40px;width:80px;">Lantern<br>Quorix</div>
  <div class="disc" style="left:26px;top:96px;width:166px;height:166px;"></div>
  <div style="position:absolute;left:54px;top:132px;">
    <h1 class="headline" style="font-size:43px;line-height:50px;color:var(--ink);">PLACE YOUR</h1>
    <h2 class="headline" style="font-size:26px;line-height:31px;color:var(--ink);">PRESENTATION TITLE HERE</h2>
    <div class="rule" style="width:50px;margin:5px 0 7px;"></div>
    <p class="detail">MORE DETAIL HERE</p>
  </div>
  <p class="fineprint" style="left:36px;top:340px;">2018 · Confidential</p>
</section>

<!-- Three column slide -->
<section class="slide slide--columns">
  <div class="disc" style="left:16px;top:14px;width:34px;height:34px;"></div>
  <div style="position:absolute;left:28px;top:24px;">
    <p class="eyebrow">MAIN THEME</p>
    <h2 class="slide-title">SLIDE TITLE HERE</h2>
  </div>
  <div class="brand brand--small" style="left:480px;top:30px;width:40px;">Lantern<br>Quorix</div>

  <div class="connector" style="left:109px;width:136px;"></div>
  <div class="connector" style="left:295px;width:136px;"></div>

  <div class="step" style="left:84px;">
    <div class="step__num">1</div>
    <p class="step__title">Place your<br>the title here</p>
    <div class="step__rule"></div>
    <p class="step__body">Lorem ipsum dolor sit amet, consectetur adipiscing elit. Quisque ornare rutrum nibh eu iaculis. Cras sed orci sit amet sapien tempor tristique ac ultricies dui.</p>
  </div>
  <div class="step" style="left:270px;">
    <div class="step__num">2</div>
    <p class="step__title">Place your<br>the title here</p>
    <div class="step__rule"></div>
    <p class="step__body">Lorem ipsum dolor sit amet, consectetur adipiscing elit. Quisque ornare rutrum nibh eu iaculis. Cras sed orci sit amet sapien tempor tristique ac ultricies dui.</p>
  </div>
  <div class="step" style="left:456px;">
    <div class="step__num">3</div>
    <p class="step__title">Place your<br>the title here</p>
    <div class="step__rule"></div>
    <p class="step__body">Lorem ipsum dolor sit amet, consectetur adipiscing elit. Quisque ornare rutrum nibh eu iaculis. Cras sed orci sit amet sapien tempor tristique ac ultricies dui.</p>
  </div>

  <p class="fineprint" style="left:38px;top:286px;">Footer here</p>
  <p class="fineprint" style="left:508px;top:286px;letter-spacing:0;">1</p>
</section>

<!-- Heavy content slide -->
<section class="slide slide--heavy">
  <div class="disc" style="left:15px;top:14px;width:30px;height:30px;"></div>
  <div style="position:absolute;left:28px;top:19px;">
    <p class="eyebrow" style="font-size:8.5px;">MAIN THEME</p>
    <h2 class="slide-title" style="font-size:16px;">SLIDE FOR HEAVY CONTENT</h2>
    <div class="rule" style="width:40px;margin-top:2px;"></div>
  </div>
  <div class="brand brand--small" style="left:463px;top:30px;width:40px;">Lantern<br>Quorix</div>
  <p class="fineprint" style="left:30px;top:286px;">Footer here</p>
  <p class="fineprint" style="left:508px;top:286px;letter-spacing:0;">1</p>
</section>

</body>
</html>
```